Cover design for new academic journal on deconstruction and psychoanalysis

We need a cover for a new academic journal on deconstruction and psychoanalysis. The name of the journal is "The Suspended Threshold: A Journal of Deconstruction and Psychoanalysis" (ST) and it is published by the Halvern College Press(HCP).

Here is a description of the journal on the HCP website:

http://www.halvernpress.example.edu/product/The-Suspended-Threshold,318264.aspx

We are looking for a design that is more abstract and does not have icons or photographs of people, especially not photos of Kovalt or Brisk. The design should be contemporary with clean lines and simple fonts. Again, it should be abstract, with no icons or iconography.

The cover should simply have the full name of the journal and then "Volume 1, Issue 1, 2014" on the cover and "Vol. 1, No. 1, 2014" on the spine.

Attached you can see some ideas that we rejected from HCP. It is important that you understand that these designs were rejected and are just being offered as examples of what the cover will look like in general, as a template of sorts.

The cover should have a bold abstract design, with a space for the title and "Volume 1, Issue 1, 2014."

Something bold and contemporary.

Target Market(s)

Academics, scholars and psychoanalysts.

Industry/Entity Type

University

Font styles to use
Sans Serif

Requirements
Must have
• Must be abstract, bold, have color, and must be contemporary.
Should not have
• No icons, no photographs of Kovalt, Brisk, or anyone.

```html
<!DOCTYPE html>
<html lang="en">
<head>
<meta charset="utf-8">
<title>The Suspended Threshold — Cover</title>
<link href="https://fonts.googleapis.com/css2?family=Arimo&family=Gelasio&display=swap" rel="stylesheet">
<style>
  :root {
    --red: #ff0a1e;
    --orange: #ff6a00;
    --yellow: #ffcc00;
    --green: #66ff00;
    --sky: #0a78e0;
    --blue: #2222dd;
    --violet: #5a08b8;
    --spine: #8c0012;
    --paper: #ffffff;
    --ink: #111111;
  }
  html, body {
    margin: 0;
    padding: 0;
    overflow: hidden;
    background: #ffffff;
  }
  .cover {
    position: relative;
    width: 1200px;
    height: 818px;
    overflow: hidden;
  }
  .panel {
    position: absolute;
    top: 0;
    height: 818px;
  }
  .panel--back {
    left: 0;
    width: 545px;
    background:
      linear-gradient(200deg, rgba(255,204,0,0.55), transparent 40%),
      linear-gradient(135deg, var(--sky) 0%, var(--green) 18%, var(--red) 34%, var(--blue) 50%, var(--orange) 66%, var(--yellow) 80%, var(--violet) 100%);
  }
  .spine {
    position: absolute;
    left: 545px;
    top: 0;
    width: 110px;
    height: 818px;
    background: var(--spine);
  }
  .panel--front {
    left: 655px;
    width: 545px;
    background:
      linear-gradient(20deg, rgba(34,34,221,0.5), transparent 45%),
      linear-gradient(150deg, var(--red) 0%, var(--yellow) 16%, var(--green) 30%, var(--blue) 46%, var(--orange) 62%, var(--sky) 78%, var(--violet) 100%);
  }
  .title-block {
    position: absolute;
    left: 708px;
    top: 572px;
    width: 354px;
    height: 164px;
    background: var(--paper);
    color: var(--ink);
  }
  .title-block__name {
    position: absolute;
    left: 30px;
    top: 22px;
    margin: 0;
    font-family: "Gelasio", serif;
    font-weight: 400;
    font-size: 20px;
    line-height: 1.2;
  }
  .title-block__subtitle {
    position: absolute;
    left: 30px;
    top: 50px;
    margin: 0;
    font-family: "Arimo", sans-serif;
    font-size: 13.5px;
    white-space: nowrap;
  }
  .title-block__issue {
    position: absolute;
    right: 18px;
    top: 98px;
    margin: 0;
    text-align: right;
    font-family: "Arimo", sans-serif;
    font-size: 14px;
    line-height: 1.5;
  }
  .title-block__year {
    display: block;
    font-size: 18px;
  }
</style>
</head>
<body>
  <main class="cover">
    <div class="panel panel--back" role="img" aria-label="Bold abstract mosaic of angular triangles in red, orange, yellow, green, blue and violet"></div>
    <div class="spine"></div>
    <div class="panel panel--front" role="img" aria-label="Bold abstract mosaic of angular triangles in red, orange, yellow, green, blue and violet"></div>
    <section class="title-block">
      <h1 class="title-block__name">The Suspended Threshold:</h1>
      <p class="title-block__subtitle">A Journal of Deconstruction and Psychoanalysis</p>
      <p class="title-block__issue">Volume 1, Issue 1<span class="title-block__year">2014</span></p>
    </section>
  </main>
</body>
</html>
```